Template design for organic gardening site for ShopTrellis platform

We need a template design for our new 'Fern Patch Naturals' shoptrellis site. Fern Patch Naturals specialises in organic nutrients for gardening plus all equipment needed to grow.
Domain name will be www.fernpatchnaturals.co.uk
Colours used should include logo colours, see attached image. Other colours to compliment the greens and lift the feel of the site could be yellow or orange.
Home page design should include, but not limited to the following:
Interactive banner carousel space
A smaller banner advertising space
Featured products
New products
Sale products feature/link
Articles links/feature
+ all standard shoptrellis features such as menus, etc
The site will be selling products (these are nutrients) such as:
Mistravelon
Heronwing soil remedy
Verdolux
Root pods
Leaf triumph
Stem wonder
Tiv
Humus prime
Terravine
+ more products and brands
Site layouts we like include:
www.fernpatchaquatics.co.uk ... A bit old fashioned but cool
www.larkplots.co.uk ... Nice but too compact
www.humusprime.com ... Has a nice top half
www.sponsorasprout.org.uk ... Nice colours and header
www.pennickbeds.co.uk ... nice layout, but needs image carousel
www.wrenseed.co.uk ... Nice background and colours
www.tulipa.co.uk ... Nice colours and layout
www.marcusbellowayplantcraft.com ... Nice layout and header
www.sprouteo.co.uk ... Cool colours and shop pages layout is nice
www.aquafarmix.co.uk ... One of the best layouts
The site should feel clean, modern and elegant.
Reason: The brief has been revised slightly and some designs we have received need to be tweeked.
Reason: We would like to see a few more designs that are on brief
Target Market(s)
Indoor and outdoor organic gardeners
Look and feel

```html
<!DOCTYPE html>
<html lang="en">
<head>
<meta charset="utf-8">
<title>Fern Patch Naturals – Home</title>
<link href="https://fonts.googleapis.com/css2?family=Roboto:wght@400;500;700&family=Roboto+Condensed:wght@400;700&display=swap" rel="stylesheet">
<style>
:root{
  --green:#6cbf2e;
  --green-dark:#4d7a3c;
  --green-link:#79c13a;
  --brown:#2b201c;
  --brown-panel:#3a2e29;
  --brown-footer:#2f2420;
  --brown-base:#251b18;
  --text-light:#e6dfd8;
  --text-muted:#a89c94;
  --line:#4c3f39;
  --gold:#9b7a12;
  --white:#fff;
}
*{margin:0;padding:0;box-sizing:border-box}
html,body{width:934px;height:1200px;overflow:hidden}
body{position:relative;font-family:"Roboto",Arial,sans-serif;background:var(--brown);color:var(--text-light)}
a{color:inherit;text-decoration:none}
.abs{position:absolute}

.topbar{left:0;top:0;width:934px;height:24px;background:var(--white);font-size:7px;color:#555}
.topbar .phone{left:477px;top:8px;font-weight:500;color:#333}
.topbar .currency{left:606px;top:8px;color:#777}
.topbar .cart{left:691px;top:7px}

.scenery{left:0;top:24px;width:934px;height:330px;
  background:linear-gradient(180deg,#5ea9e0 0%,#a9d6f2 45%,#cfe9f6 58%,#7fb43a 64%,#4f8a2a 72%,#2f4a22 84%,var(--brown) 100%)}

.logo{left:230px;top:44px;display:flex;align-items:center;gap:8px}
.logo .mark{width:40px;height:40px;background:var(--green-dark);border-radius:4px}
.logo .name{font-family:"Roboto Condensed",sans-serif;font-weight:700;font-size:19px;color:var(--green-dark);line-height:1.05;width:110px}

.search{left:570px;top:60px;width:134px;height:20px;background:var(--white);border:1px solid #9fc6e6;font-size:7px;color:#666;padding:6px 8px}
.search svg{position:absolute;right:6px;top:5px}

.mainnav{left:230px;top:98px;width:474px;height:21px;border-bottom:2px solid rgba(255,255,255,.5);font-size:7px;color:#3d4f5c}
.mainnav a{position:absolute;top:0}

.banner{left:230px;top:133px;width:474px;height:217px;background:var(--white)}
.banner .photo{position:absolute;left:9px;top:9px;width:210px;height:200px;background:linear-gradient(135deg,#7a8f55,#2e2a26 60%,#5f6a3a)}
.banner .panel{position:absolute;left:219px;top:9px;width:237px;height:200px;background:var(--green-dark);overflow:hidden}
.banner .leaves{position:absolute;left:0;top:0;width:110px;height:200px;background:radial-gradient(ellipse at 30% 50%,#6cbf2e 0%,#5aa52e 40%,transparent 70%)}
.banner h2{position:absolute;left:100px;top:30px;font-family:"Roboto Condensed",sans-serif;font-weight:700;font-size:18px;line-height:20px;color:var(--white)}
.banner ul{position:absolute;left:100px;top:79px;list-style:none;font-family:"Roboto Condensed",sans-serif;font-size:8.5px;color:var(--white)}
.banner li{height:15px}
.banner li::before{content:"";display:inline-block;width:3px;height:3px;background:var(--green);margin-right:4px;vertical-align:middle}
.banner .price{position:absolute;left:101px;top:130px;font-family:"Roboto Condensed",sans-serif;font-weight:700;font-size:8.5px;color:var(--white)}
.banner .cta{position:absolute;left:102px;top:151px;width:95px;height:23px;background:var(--green);color:var(--white);font-size:8.5px;font-weight:500;padding:7px 9px}
.banner .cta svg{position:absolute;right:7px;top:5px}
.ribbon{position:absolute;top:0;right:0;overflow:hidden}
.arrow{width:23px;height:28px;background:var(--white);top:226px;border-radius:3px;color:#333;font-size:14px;text-align:center;line-height:28px}

.dots{left:449px;top:358px;display:flex;gap:6px}
.dots span{width:8px;height:8px;border-radius:50%;background:#d9c98a;border:1px solid #9c8c50}
.dots span:first-child{background:#f2f2e6;border-color:var(--green-dark)}

.section-title{left:230px;font-size:14px;font-weight:400;color:#eee}
.products{left:230px;width:474px;background:var(--brown-panel);padding:10px 9px}
.products ul{list-style:none;display:flex;gap:12px}
.product{width:105px;position:relative}
.product .thumb{width:105px;height:105px;position:relative;overflow:hidden}
.product .name{font-size:7px;line-height:11.5px;color:var(--text-light);margin-top:12px;height:23px;width:94px;overflow:hidden}
.product .tag{display:block;background:var(--gold);color:#fff;font-size:6.5px;line-height:10px;padding:0 6px;width:77px;margin-top:1px}
.product .price{font-size:7px;color:var(--green-link);font-weight:500;margin-top:5px}
.btn{display:inline-block;background:var(--green);color:var(--white);font-size:7px;font-weight:500;text-align:center}
.product .btn{width:67px;height:19px;line-height:19px;margin-top:10px}

.footer{left:0;top:896px;width:934px;height:246px;background:var(--brown-footer)}
.col{top:34px;width:104px}
.col h3{font-size:10px;font-weight:400;color:#e8e2dc;padding-bottom:10px;border-bottom:1px solid var(--line);margin-bottom:11px}
.col ul{list-style:none;font-size:7px;color:var(--green-link)}
.col li{height:15.2px}
.updates dt{font-size:6px;color:#ddd;margin-top:1px}
.updates dd{font-size:7px;color:var(--green-link);line-height:11px;margin-bottom:11px}
.newsletter p{font-size:7px;color:#ddd}
.newsletter .field{width:104px;height:16px;background:#5e504a;border:1px solid #7a6d66;font-size:6px;font-style:italic;color:#eee;padding:4px 5px;margin-top:12px}
.newsletter .field+.field{margin-top:8px}
.newsletter .btn{width:48px;height:19px;line-height:19px;margin-top:12px}
.newsletter h4{font-size:10px;font-weight:400;color:#e8e2dc;margin-top:28px}
.social{display:flex;gap:7px;margin-top:7px}
.social span{width:11px;height:11px;background:var(--green-dark)}

.bottombar{left:0;top:1142px;width:934px;height:58px;background:var(--brown-base);font-size:7px}
.bottombar a{position:absolute;top:17px;font-weight:500;color:#eee}
.bottombar small{position:absolute;left:240px;top:33px;font-size:5.5px;color:var(--text-muted)}
</style>
</head>
<body>

<div class="abs scenery" role="img" aria-label="Blue sky with clouds, hanging leaves and a strip of green grass"></div>

<header class="abs topbar">
  <span class="abs phone">Telephone us on 01632 960 418</span>
  <span class="abs currency">All prices are in &nbsp;£GBP</span>
  <svg class="abs cart" width="10" height="9" viewBox="0 0 10 9"><path d="M1 3h8l-1 5H2z" fill="none" stroke="#777" stroke-width="1"/><path d="M3 3l2-2 2 2" fill="none" stroke="#777"/></svg>
</header>

<a class="abs logo" href="#"><span class="mark"></span><span class="name">Fern Patch Naturals</span></a>

<div class="abs search">Search
  <svg width="9" height="9" viewBox="0 0 9 9"><circle cx="5.5" cy="3.5" r="2.7" fill="none" stroke="#7aa8cf"/><path d="M3.5 5.5L1 8" stroke="#7aa8cf" stroke-width="1.3"/></svg>
</div>

<nav class="abs mainnav">
  <a style="left:0">Home</a><a style="left:44px">About Us</a><a style="left:99px">Our Products</a><a style="left:168px">Sale</a><a style="left:206px">FAQs</a><a style="left:248px">Contact Us</a>
</nav>

<section class="abs banner">
  <div class="photo" role="img" aria-label="Bags and tub of tree care products on a garden lawn"></div>
  <div class="panel">
    <div class="leaves" role="img" aria-label="Large green leaf decoration"></div>
    <h2>RootChar Tree<br>Care Bundle</h2>
    <ul><li>5kg Tree Growth Enhancer</li><li>5kg Tree Protector</li><li>2.5kg Fertiliser</li></ul>
    <p class="price">NOW ONLY £49.99</p>
    <a class="cta" href="#">Add to basket
      <svg width="13" height="12" viewBox="0 0 13 12"><path d="M1 4h11l-1.5 7h-8z" fill="none" stroke="#fff"/><path d="M4 4l2.5-3 2.5 3" fill="none" stroke="#fff"/></svg>
    </a>
    <svg class="ribbon" width="70" height="70" viewBox="0 0 70 70"><path d="M14 0h22l34 34v22z" fill="#6cbf2e"/><text x="42" y="30" transform="rotate(45 42 30)" font-family="Roboto Condensed,sans-serif" font-weight="700" font-size="12" fill="#fff" text-anchor="middle">SALE</text></svg>
  </div>
</section>
<div class="abs arrow" style="left:230px">‹</div>
<div class="abs arrow" style="left:681px">›</div>
<div class="abs dots"><span></span><span></span><span></span></div>

<h2 class="abs section-title" style="top:383px">Featured Products</h2>
<section class="abs products" style="top:410px;height:206px">
  <ul>
    <li class="product"><div class="thumb" role="img" aria-label="Black bag of growth enhancer beside a garden spade" style="background:linear-gradient(160deg,#5d7a3a,#1f1f1f)"></div>
      <p class="name">Product name to go on this space here</p><p class="price">£20.00</p><a class="btn">Add to basket</a></li>
    <li class="product"><div class="thumb" role="img" aria-label="Colourful nutrient packets and tablets on grass" style="background:linear-gradient(160deg,#e9e2d2,#c9a25a 50%,#5f8f3a)"></div>
      <p class="name">Product name to go on this space here</p><p class="price">£20.00</p><a class="btn">Add to basket</a></li>
    <li class="product"><div class="thumb" role="img" aria-label="Two tubs of granular plant feed" style="background:linear-gradient(160deg,#f4f4f4,#3a3a3a 60%,#e8e8e8)">
        <svg class="ribbon" width="50" height="50" viewBox="0 0 50 50"><path d="M10 0h16l24 24v16z" fill="#6cbf2e"/><text x="30" y="22" transform="rotate(45 30 22)" font-size="8" font-weight="700" fill="#fff" text-anchor="middle" font-family="Roboto Condensed,sans-serif">SALE</text></svg></div>
      <p class="name">Product name to go on this space here</p><p class="price">£20.00</p><a class="btn">Add to basket</a></li>
    <li class="product"><div class="thumb" role="img" aria-label="Tube of granules on dark soil with blue sparkles" style="background:radial-gradient(circle at 50% 40%,#4e8a6a,#1b2225 70%)"></div>
      <p class="name">Product name to go on this space here</p><p class="price">£20.00</p><a class="btn">Add to basket</a></li>
  </ul>
</section>

<h2 class="abs section-title" style="top:635px">New Products</h2>
<section class="abs products" style="top:661px;height:207px">
  <ul>
    <li class="product"><div class="thumb" role="img" aria-label="Tubs of organic fertiliser among leaves" style="background:linear-gradient(160deg,#7f9a4a,#222 55%,#5e7a30)"></div>
      <p class="name">Product name to go on this space here</p><p class="price">£20.00</p><a class="btn">Add to basket</a></li>
    <li class="product"><div class="thumb" role="img" aria-label="Two bottles of liquid plant nutrient" style="background:linear-gradient(90deg,#fff 10%,#2f5a3a 30%,#f3f3f3 50%,#b84a5a 70%,#fff 90%)">
        <svg class="ribbon" width="50" height="50" viewBox="0 0 50 50"><path d="M10 0h16l24 24v16z" fill="#6cbf2e"/><text x="30" y="22" transform="rotate(45 30 22)" font-size="8" font-weight="700" fill="#fff" text-anchor="middle" font-family="Roboto Condensed,sans-serif">SALE</text></svg></div>
      <p class="name">Product name to in here<span class="tag">Introductory Offer</span></p><p class="price">£20.00</p><a class="btn">Add to basket</a></li>
    <li class="product"><div class="thumb" role="img" aria-label="Bags of compost in a flowering garden bed" style="background:linear-gradient(160deg,#6a8f4a,#3c3a30 55%,#7a6a4a)">
        <svg class="ribbon" width="50" height="50" viewBox="0 0 50 50"><path d="M10 0h16l24 24v16z" fill="#6cbf2e"/><text x="30" y="22" transform="rotate(45 30 22)" font-size="8" font-weight="700" fill="#fff" text-anchor="middle" font-family="Roboto Condensed,sans-serif">SALE</text></svg></div>
      <p class="name">Product name to go &nbsp;here<span class="tag">Introductory Offer</span></p><p class="price">£20.00</p><a class="btn">Add to basket</a></li>
    <li class="product"><div class="thumb" role="img" aria-label="White tub of soil conditioner with a scoop of granules" style="background:linear-gradient(180deg,#fff 40%,#e8d8d0 70%,#8a5a3a)"></div>
      <p class="name">Product name to go on this space here</p><p class="price">£20.00</p><a class="btn">Add to basket</a></li>
  </ul>
</section>

<footer class="abs footer">
  <div class="abs col" style="left:240px"><h3>Popular Brands</h3>
    <ul><li>Mistravelon</li><li>Heronwing soil remedy</li><li>Verdolux</li><li>Root pods</li><li>Leaf triumph</li><li>Stem wonder</li><li>Tiv</li><li>Humus prime</li><li>Terravine</li></ul></div>
  <div class="abs col" style="left:356px"><h3>Categories</h3>
    <ul><li>Complete Grow Kits</li><li>Plant Lighting</li><li>Environment Control</li><li>Grow Tents</li><li>Grow Systems</li><li>Grow Mediums</li><li>Pots and Trays</li><li>Nutrients and Additives</li><li>Nutrient Control</li><li>Pumps &amp; Tank Heaters</li></ul></div>
  <div class="abs col updates" style="left:473px"><h3>Recent Updates</h3>
    <dl><dt>NEW PRODUCT</dt><dd>Product title in this space</dd>
      <dt>NEWS STORY</dt><dd>News article title to be placed in this space here</dd>
      <dt>NEW PRODUCT</dt><dd>Product title in this space</dd>
      <dt>NEW PRODUCT</dt><dd>Product title in here</dd></dl></div>
  <div class="abs col newsletter" style="left:590px"><h3>Newsletter</h3>
    <p>Sign up for our newsletter here</p>
    <div class="field">Name</div><div class="field">Email Address</div>
    <a class="btn">Sign Up</a>
    <h4>Connect with us</h4>
    <div class="social"><span></span><span></span><span></span></div></div>
</footer>

<div class="abs bottombar">
  <a style="left:240px">Home</a><a style="left:283px">About Us</a><a style="left:338px">Our Products</a><a style="left:407px">Sale</a><a style="left:446px">FAQs</a><a style="left:486px">Contact Us</a>
  <small>© 2015 Fern Patch Naturals . All rights reserved</small>
</div>

</body>
</html>
```